Oversize Postcard for Harborline Rinseworks USA

Please use already created postcard named "Postcard Design project template" that's in my Printerley portfolio (acct# 2940-3176-5528. It has the photos I want and the text that is appropriate etc. I just you you guys to make it look more professional and polished
Updates

Target Market(s)

Residential and commercial property owners

Font styles to use
Serif

Requirements
Must have
• Pictures and background graphic attached
Nice to have
• Need the postcard to be professional looking
Should not have
• Not sure

```html
<!DOCTYPE html>
<html lang="en">
<head>
<meta charset="utf-8">
<title>Softwash Postcard</title>
<link href="https://fonts.googleapis.com/css2?family=Oswald:wght@600;700&family=Archivo+Black&family=Libre+Baskerville:wght@700&display=swap" rel="stylesheet">
<style>
  :root{
    --backdrop:#2b2b2b;
    --navy:#0b4f96;
    --headline-blue:#1c4f93;
    --alert-red:#d5232b;
    --sky-blue:#22a4ea;
    --white:#ffffff;
    --wave-grey:#c9cdd3;
    --eco-green:#8cc63f;
    --eco-dark:#1f7a34;
  }
  *{margin:0;padding:0;box-sizing:border-box}
  html,body{width:1200px;height:923px;overflow:hidden;background:var(--backdrop)}
  .postcard{position:absolute;left:95px;top:72px;width:1010px;height:778px;overflow:hidden;
    background:linear-gradient(180deg,#7fa9d6 0%,#b4cde6 45%,#dfe8f1 70%);}
  .house-photo{position:absolute;left:505px;top:0;width:505px;height:470px;
    background:linear-gradient(160deg,#9fc0e3 0%,#5a5552 30%,#4a4340 55%,#7a2e22 80%,#8e3a2c 100%);}
  .wave{position:absolute;left:0;top:0;width:1010px;height:778px}
  .headline{position:absolute;left:50px;top:70px;font-family:"Oswald",sans-serif;font-weight:700;
    color:var(--headline-blue);font-size:40px;line-height:44px;letter-spacing:.3px;
    text-shadow:0 0 14px #fff,0 0 8px #fff}
  .headline-hook{position:absolute;left:44px;top:160px;font-family:"Oswald",sans-serif;font-weight:700;
    color:var(--alert-red);font-size:74px;line-height:84px;text-shadow:0 0 16px #fff,0 0 8px #fff}
  .result-photo{position:absolute;width:231px;height:180px;border:6px solid var(--white);}
  .result-photo span{position:absolute;bottom:4px;font-family:"Libre Baskerville",serif;font-weight:700;
    font-size:14px;color:var(--white);text-shadow:1px 1px 2px #000}
  .roof-before{left:36px;top:266px;background:linear-gradient(160deg,#b87a52,#9a6a45 60%,#7d6a44)}
  .roof-after{left:290px;top:266px;background:linear-gradient(160deg,#c9865a,#d88a55 60%,#b8794c)}
  .siding-before{left:36px;top:473px;background:linear-gradient(100deg,#7a5a35 0 12%,#c8c9ad 14%,#a3ab86 70%,#8c9a6f)}
  .siding-after{left:290px;top:473px;background:linear-gradient(100deg,#8a5f35 0 24%,#f2efe2 26%,#e8e5d6)}
  .roof-before span,.siding-before span{left:22px}
  .roof-after span,.siding-after span{left:28px}
  .siding-before span{left:auto;right:16px;font-size:11px}
  .siding-after span{left:auto;right:28px;font-size:11px}
  .eco-badge{position:absolute;left:796px;top:298px;width:180px;height:180px}
  .services{position:absolute;left:548px;top:500px;font-family:"Archivo Black",sans-serif}
  .services-main{color:var(--sky-blue);font-size:34px;line-height:40px;letter-spacing:.5px}
  .services-sub{color:var(--white);font-size:25px;line-height:31px;margin-top:6px}
  .promise{position:absolute;left:0;width:1010px;top:686px;text-align:center;font-family:"Oswald",sans-serif;
    font-weight:600;font-size:25px;color:var(--sky-blue);letter-spacing:.3px}
  .compliance{position:absolute;left:0;width:1010px;top:722px;text-align:center;font-family:"Oswald",sans-serif;
    font-weight:700;font-size:29px;color:var(--white)}
</style>
</head>
<body>
<div class="postcard">
  <div class="house-photo" role="img" aria-label="Photo of a red brick house with a clean dark tiled roof and white dormer window"></div>
  <svg class="wave" viewBox="0 0 1010 778" aria-hidden="true">
    <path d="M0,412 C160,350 360,392 520,372 C650,356 700,448 800,446 C900,444 960,410 1010,392 L1010,778 L0,778Z" fill="var(--wave-grey)"/>
    <path d="M0,432 C160,368 360,410 520,392 C650,376 700,468 800,464 C900,462 960,430 1010,412 L1010,778 L0,778Z" fill="var(--navy)"/>
  </svg>

  <h1 class="headline">PROPERTY GOT DIRT,<br>GRIME, MOLD, MILDEW?</h1>
  <p class="headline-hook">GOT SCHMUTZ?</p>

  <div class="result-photo roof-before" role="img" aria-label="Tile roof covered in mold before cleaning"><span>BEFORE</span></div>
  <div class="result-photo roof-after" role="img" aria-label="Tile roof clean after softwash"><span>AFTER</span></div>
  <div class="result-photo siding-before" role="img" aria-label="Vinyl siding with green mildew before cleaning"><span>BEFORE</span></div>
  <div class="result-photo siding-after" role="img" aria-label="Clean white vinyl siding after cleaning"><span>AFTER</span></div>

  <svg class="eco-badge" viewBox="0 0 180 180" role="img" aria-label="Always eco safe badge">
    <circle cx="90" cy="90" r="88" fill="var(--white)"/>
    <circle cx="90" cy="90" r="80" fill="var(--eco-green)"/>
    <text x="90" y="66" text-anchor="middle" font-family="Oswald, sans-serif" font-weight="700" font-size="28" fill="#fff" stroke="var(--eco-dark)" stroke-width="1.2">ALWAYS</text>
    <text x="90" y="98" text-anchor="middle" font-family="Oswald, sans-serif" font-weight="700" font-size="28" fill="#fff" stroke="var(--eco-dark)" stroke-width="1.2">ECO SAFE</text>
    <path d="M88,158 C60,150 52,125 62,104 C80,112 94,130 88,158Z" fill="var(--eco-dark)"/>
    <path d="M94,158 C122,150 128,122 118,100 C100,110 88,132 94,158Z" fill="var(--eco-dark)"/>
  </svg>

  <div class="services">
    <p class="services-main">PRESSURE WASH<br>SOFTWASH SERVICES</p>
    <p class="services-sub">EXTERIOR CLEANING<br>&amp; SANITIZING</p>
  </div>

  <p class="promise">WE OFFER CHEAPER-FASTER-QUIETER-SAFER AND LONGER LASTING RESULTS</p>
  <p class="compliance">DROUGHT ORDINANCE COMPLAINT</p>
</div>
</body>
</html>
```